Your conflict - our mediation - joint conflict SOLUTION

With this flyer I am looking for conflict parties who are ready to tackle and resolve their conflict with a prospective mediator. The mediation is free because I am doing it as part of my diploma thesis. Time frame approx. 4 sessions of 2.5 hours each. The wishes and needs of both parties are listened to and “picked out”. In an open, constructive, appreciative framework, solutions are developed and negotiated together.

Target Market(s)

everyone who is ready to deal with himself and his counterpart and everyone who wants to work out a solution with the respect, openness and support of a mediator.

Requirements
Must have
• - "For my diploma thesis I am looking for conflicting parties who are willing to resolve their conflict with a mediator"
- Time frame: 4 x 2.5 hours feasible in Solothurn, Bern, Brugg
- Free of charge
- my coordinates - see business card
- more information at www.lindenhofwerk.ch
Nice to have
• the card should be based on the style of my homepage www.lindenhofwerk.ch and my business card

```html
<!DOCTYPE html>
<html lang="en">
<head>
<meta charset="utf-8">
<title>Conflict Dispute Blockade – Finding Solutions Together</title>
<link rel="stylesheet" href="https://fonts.googleapis.com/css2?family=Raleway:wght@400;500;600;700&display=swap">
<style>
  :root {
    --gold: #b09655;
    --olive: #8f9a2c;
    --purple: #6a4fb3;
    --lime: #d9e85a;
    --ink: #2a2a2a;
    --slate: #333d3d;
    --grey-bar: #e6e8e8;
    --muted: #cfd4d4;
    --white: #ffffff;
  }
  * { box-sizing: border-box; margin: 0; padding: 0; }
  html, body { width: 848px; height: 1200px; overflow: hidden; background: var(--white); }
  body { font-family: "Raleway", sans-serif; color: var(--ink); }
  .flyer { position: relative; width: 848px; height: 1200px; overflow: hidden; background: var(--white); }
  .hero-photo {
    position: absolute; left: 0; top: 0; width: 848px; height: 660px;
    background: linear-gradient(160deg, #d9dde2 0%, #eef1f4 35%, #c9d8e8 55%, #cfe3cf 80%, #e8d8c4 100%);
  }
  .shape-layer { position: absolute; left: 0; top: 0; width: 848px; height: 1200px; }
  .brand {
    position: absolute; left: 0; width: 848px; top: 610px;
    display: flex; justify-content: center; align-items: center; gap: 8px;
    padding-right: 200px;
  }
  .brand-dot { width: 14px; height: 14px; border-radius: 50%; background: var(--gold); }
  .brand-name { font-size: 26px; font-weight: 600; color: var(--gold); letter-spacing: 0.5px; }
  .title {
    position: absolute; left: 98px; top: 684px;
    font-size: 31px; font-weight: 700; color: var(--gold); letter-spacing: -0.3px;
  }
  .subtitle-bar { position: absolute; left: 98px; top: 734px; width: 165px; height: 11px; background: var(--grey-bar); }
  .subtitle {
    position: absolute; left: 268px; top: 729px;
    font-size: 17px; font-weight: 500; color: var(--ink);
  }
  .intro { position: absolute; left: 34px; top: 782px; width: 395px; }
  .intro h2 { font-size: 17px; font-weight: 600; margin-bottom: 10px; }
  .intro p { font-size: 14.3px; line-height: 20.5px; text-align: justify; margin-bottom: 12px; }
  .about { position: absolute; left: 28px; top: 973px; width: 418px; }
  .about h3 {
    display: inline-block; font-size: 17.5px; font-weight: 600;
    border-bottom: 1px dashed var(--ink); margin-bottom: 8px; line-height: 22px;
  }
  .about p { font-size: 17.5px; line-height: 24px; text-align: justify; }
  .details-card {
    position: absolute; left: 469px; top: 770px; width: 400px; height: 330px;
    background: var(--white); box-shadow: -3px 2px 6px rgba(0,0,0,0.18);
  }
  .quote {
    position: absolute; left: 497px; top: 784px; width: 320px;
    font-size: 14.5px; line-height: 20px; color: var(--olive); text-align: justify;
    padding-left: 23px;
  }
  .quote::before {
    content: "\201C"; position: absolute; left: 0; top: -6px;
    font-size: 32px; font-weight: 700; font-family: Georgia, serif; color: var(--olive);
  }
  .quote-close { font-size: 32px; font-weight: 700; font-family: Georgia, serif; line-height: 0; vertical-align: -12px; margin-left: 4px; }
  .facts { position: absolute; left: 496px; top: 880px; list-style: none; }
  .facts li {
    display: flex; align-items: center; gap: 14px; height: 39px;
    font-size: 18px; color: var(--ink);
  }
  .facts li::before {
    content: ""; flex: none; width: 15px; height: 15px; border-radius: 50%;
    background: var(--slate);
  }
  .footer-text { position: absolute; color: var(--white); }
  .call { left: 28px; top: 1131px; display: flex; align-items: center; gap: 10px; font-size: 19px; font-weight: 500; }
  .call svg { width: 27px; height: 27px; }
  .more { right: 24px; top: 1096px; width: 300px; text-align: center; }
  .more .lead { font-size: 15.5px; font-weight: 500; line-height: 20px; margin-bottom: 4px; }
  .more .line { font-size: 14.5px; color: var(--muted); line-height: 24px; }
</style>
</head>
<body>
<div class="flyer">
  <div class="hero-photo" role="img" aria-label="Photo of a mediator with a clipboard in conversation with a man and a woman in a bright room"></div>

  <svg class="shape-layer" viewBox="0 0 848 1200" aria-hidden="true">
    <path d="M0,535 Q420,470 700,640 L720,640 L848,595 L848,1200 L0,1200 Z" fill="var(--white)"/>
    <path d="M0,543 Q420,478 662,628 Q400,512 0,574 Z" fill="var(--purple)"/>
    <path d="M0,588 Q420,528 662,646 Q400,556 0,613 Z" fill="var(--lime)"/>
  </svg>

  <div class="brand">
    <span class="brand-dot"></span>
    <span class="brand-name">Lindenhofwerk</span>
  </div>

  <h1 class="title">CONFLICT DISPUTE BLOCKADE</h1>
  <div class="subtitle-bar"></div>
  <p class="subtitle">FINDING SOLUTIONS TOGETHER</p>

  <section class="intro">
    <h2>Are you stuck with your familiar one?</h2>
    <p>I am here to find a coherent, sustainable solution that has been worked out jointly and that makes constructive interaction between the conflicting parties.</p>
    <p>The conflicting parties workout a solution themselves, accompanied and guided by a mediator.</p>
  </section>

  <section class="about">
    <h3>About me</h3>
    <p>I am a mediator, coach, lecturer, lawyer, social security specialist, and examination expert.</p>
  </section>

  <div class="details-card"></div>
  <p class="quote">For my diploma thesis I am looking for conflicting parties who are willing to resolve their conflict with a mediator.<span class="quote-close">&#8221;</span></p>
  <ul class="facts">
    <li>Time frame: 4 x 2.5 hours</li>
    <li>Feasible in Solothurn, Bern, Brugg</li>
    <li>Free of charge</li>
    <li>My coordinates - see business card</li>
  </ul>
  <svg class="shape-layer" viewBox="0 0 848 1200" aria-hidden="true">
    <g fill="none" stroke="var(--white)" stroke-width="1.6" stroke-linecap="round" stroke-linejoin="round">
      <polyline points="502,896 505,899 502,902"/>
      <polyline points="502,935 505,938 502,941"/>
      <polyline points="502,974 505,977 502,980"/>
      <polyline points="502,1013 505,1016 502,1019"/>
    </g>
  </svg>

  <svg class="shape-layer" viewBox="0 0 848 1200" aria-hidden="true">
    <path d="M0,1072 Q300,1052 490,1200 L0,1200 Z" fill="var(--lime)"/>
    <path d="M0,1080 Q290,1064 474,1200 L0,1200 Z" fill="var(--slate)"/>
    <path d="M372,1200 C432,1100 548,1064 848,1050 L848,1200 Z" fill="var(--lime)"/>
    <path d="M392,1200 C450,1110 560,1075 848,1060 L848,1200 Z" fill="var(--slate)"/>
  </svg>

  <div class="footer-text call">
    <svg viewBox="0 0 27 27" aria-hidden="true">
      <rect x="1" y="1" width="25" height="25" fill="none" stroke="var(--white)" stroke-width="1.6"/>
      <path d="M8,6 L11,6 L12.5,10 L10.5,11.5 Q12.5,15.5 15.5,16.5 L17,14.5 L21,16 L21,19 Q20,21 18,21 Q8,19 6,8 Q6,6 8,6 Z" fill="none" stroke="var(--white)" stroke-width="1.5" stroke-linejoin="round"/>
    </svg>
    <span>Call now @ (455) 987 654 321</span>
  </div>

  <div class="footer-text more">
    <p class="lead">For more information visit:</p>
    <p class="line">www.lindenhofwerk.ch</p>
    <p class="line">Mail us to : support@lindenhofwerk.ch</p>
  </div>
</div>
</body>
</html>
```